Buch-/eBook-Cover für Esoterikbuch
Alle meine Änderungswünsche wurden zeitnah umgesetzt. Als es nach der Dateiübergabe technische Probleme gab, weil ich den Buchinhalt falsch formatiert hatte, hat die Designerin viel Geduld bewiesen und das Cover dann klaglos an die neuen Formate angepasst. Ich werde jederzeit gerne wieder mit ihr zusammenarbeiten.
Zielgruppe
Ebook- und Taschenbuchcover für ein Esoterikbuch über Quantenheilung auf Vendura. Details befinden sich im Anhang.
Aufgabenstellung
Keine besonderen Vorgaben.

```html
<!DOCTYPE html>
<html lang="de">
<head>
<meta charset="utf-8">
<title>Quantenheilung und Bewusstsein – Buchcover</title>
<link rel="stylesheet" href="https://fonts.googleapis.com/css2?family=Rubik:wght@400;500;600;700&display=swap">
<style>
  :root {
    --page-bg: #e3e3e5;
    --navy-deep: #151d4d;
    --navy: #1a2766;
    --blue-mid: #1f4fb0;
    --glow-cyan: rgba(140, 225, 255, 0.9);
    --glow-blue: rgba(70, 140, 255, 0.55);
    --glow-pink: rgba(225, 110, 200, 0.45);
    --band-white: #f4f5f7;
    --title-ink: #16204a;
    --text-light: #ffffff;
  }
  * { box-sizing: border-box; margin: 0; padding: 0; }
  html, body {
    width: 1200px;
    height: 899px;
    overflow: hidden;
    background: var(--page-bg);
    font-family: "Rubik", sans-serif;
  }
  .canvas {
    width: 1200px;
    height: 899px;
    display: flex;
    align-items: center;
    justify-content: center;
  }
  .cover {
    position: relative;
    width: 540px;
    height: 810px;
    background: linear-gradient(180deg, var(--navy-deep) 0%, var(--navy) 30%, #1c3a94 100%);
    overflow: hidden;
  }
  .cover-art {
    position: absolute;
    left: 0;
    right: 0;
    top: 270px;
    bottom: 0;
    background:
      radial-gradient(ellipse 34% 20% at 52% 20%, var(--glow-pink) 0%, rgba(225, 110, 200, 0) 100%),
      radial-gradient(ellipse 36% 24% at 48% 30%, var(--glow-cyan) 0%, rgba(90, 170, 255, 0.5) 40%, rgba(40, 90, 200, 0) 100%),
      radial-gradient(ellipse 90% 45% at 50% 82%, var(--glow-blue) 0%, rgba(30, 80, 200, 0) 100%),
      radial-gradient(ellipse 60% 30% at 15% 95%, rgba(60, 130, 255, 0.45) 0%, rgba(30, 80, 200, 0) 100%),
      radial-gradient(ellipse 60% 30% at 85% 95%, rgba(60, 130, 255, 0.45) 0%, rgba(30, 80, 200, 0) 100%),
      linear-gradient(180deg, #17296f 0%, #1b3f9c 55%, #1f4fb4 100%);
  }
  .author {
    position: absolute;
    top: 32px;
    left: 0;
    right: 0;
    text-align: center;
    color: var(--text-light);
    font-size: 21px;
    font-weight: 500;
  }
  .title-band {
    position: absolute;
    top: 74px;
    left: 0;
    right: 0;
    height: 196px;
    background: var(--band-white);
    display: flex;
    flex-direction: column;
    align-items: flex-end;
    justify-content: center;
    padding-right: 22px;
    color: var(--title-ink);
  }
  .title-main {
    font-size: 66px;
    font-weight: 700;
    line-height: 1.05;
    letter-spacing: -1px;
  }
  .title-sub {
    font-size: 56px;
    font-weight: 400;
    line-height: 1.1;
    letter-spacing: -0.5px;
  }
  .subtitle {
    position: absolute;
    top: 585px;
    left: 30px;
    right: 30px;
    text-align: center;
    color: var(--text-light);
    font-size: 30px;
    font-weight: 600;
    line-height: 1.15;
    letter-spacing: -0.3px;
    text-shadow: 0 1px 6px rgba(10, 20, 60, 0.55);
  }
</style>
</head>
<body>
  <main class="canvas">
    <article class="cover">
      <div class="cover-art" role="img" aria-label="Leuchtendes Gehirn über einem blauen, vernetzten Lichtgitter im Sternenraum"></div>
      <p class="author">Henrik Sonnwald</p>
      <header class="title-band">
        <h1 class="title-main">Quantenheilung</h1>
        <p class="title-sub">und Bewusstsein</p>
      </header>
      <p class="subtitle">Wie Sie Zugriff auf<br>die Informationsebene<br>der Realität nehmen</p>
    </article>
  </main>
</body>
</html>
```